Stationary
Vela Rigs
Use same font as used in my logo
Use a complement to the logo font
Professional
Tom Baxter
Owner/Installation Consultant
5678 Halloway Dr.
Alder Falls ON, K7P 5R9
tom@velarigs.com
www.velarigs.com

```html
<!DOCTYPE html>
<html lang="en">
<head>
<meta charset="utf-8">
<title>Vela Rigs — Stationery Concepts</title>
<link href="https://fonts.googleapis.com/css2?family=Michroma&family=Montserrat:wght@400;600&display=swap" rel="stylesheet">
<style>
  :root {
    --backdrop: #e9e4dc;
    --paper: #ffffff;
    --ink: #1c1c1c;
    --ink-soft: #6d6d6d;
    --brand-red: #b3151b;
    --label: #4b443c;
    --display: "Michroma", sans-serif;
    --body: "Montserrat", sans-serif;
  }
  * { box-sizing: border-box; margin: 0; padding: 0; }
  html, body { width: 1200px; height: 631px; overflow: hidden; }
  body { background: var(--backdrop); position: relative; font-family: var(--body); color: var(--ink); }

  .label {
    position: absolute; font-family: var(--display); font-size: 6px;
    letter-spacing: 1.4px; text-transform: uppercase; color: var(--label); white-space: nowrap;
    transform: translateX(-50%);
  }
  .label--section { font-size: 7px; letter-spacing: 1.5px; left: 53px; top: 170px; transform: none; }

  .piece { position: absolute; overflow: hidden; box-shadow: 0 2px 6px rgba(0,0,0,.25); }
  .piece svg.swoosh { position: absolute; left: 0; bottom: 0; width: 100%; }

  .brand { display: flex; align-items: center; gap: 5px; font-family: var(--display); color: var(--brand-red); white-space: nowrap; }
  .brand__dot { width: 8px; height: 8px; border-radius: 50%; background: var(--brand-red); flex: none; }

  /* Business cards */
  .card { left: 36px; width: 168px; height: 89px; background: linear-gradient(160deg, #3a3a3a, #0d0d0d 70%); }
  .card--front { top: 228px; }
  .card--back { top: 348px; }
  .card--front .brand { position: absolute; left: 8px; top: 40px; font-size: 6.5px; gap: 4px; }
  .card--front .brand__dot { width: 6px; height: 6px; }
  .card__details { position: absolute; left: 84px; top: 22px; font-size: 4.5px; line-height: 1.6; color: #d6d6d6; white-space: nowrap; }
  .card__name { font-family: var(--display); font-size: 5.5px; color: #fff; }
  .card--back .brand { position: absolute; left: 50%; top: 50%; transform: translate(-50%,-50%); font-size: 10px; }

  /* Letterhead */
  .letterhead { left: 230px; top: 43px; width: 399px; height: 514px; background: var(--paper); }
  .letterhead .brand--top { position: absolute; left: 24px; top: 22px; font-size: 10px; }
  .letterhead__contact { position: absolute; left: 290px; top: 16px; font-size: 5px; line-height: 1.7; color: var(--ink-soft); white-space: nowrap; }
  .letterhead__contact span::before { content: ""; display: inline-block; width: 3px; height: 3px; background: var(--brand-red); margin-right: 3px; vertical-align: middle; }
  .letterhead__mark { position: absolute; left: 50%; top: 240px; transform: translateX(-50%); font-family: var(--display); font-size: 28px; color: #eeeeee; white-space: nowrap; }

  /* Envelopes */
  .envelope { left: 696px; width: 408px; background: var(--paper); }
  .envelope--red { top: 65px; height: 100px; }
  .envelope--dark { top: 149px; height: 120px; }
  .envelope--white { top: 259px; height: 110px; background: #f6f6f6; }
  .envelope .flap { position: absolute; left: 0; top: 0; width: 100%; }
  .envelope--white .brand { position: absolute; left: 50%; top: 38px; transform: translateX(-50%); font-size: 7px; }
  .envelope--front { left: 662px; top: 360px; width: 442px; height: 197px; background: var(--paper); }
  .envelope--front .brand { position: absolute; left: 22px; top: 24px; font-size: 9px; }
  .envelope__return { position: absolute; left: 22px; top: 44px; font-size: 5px; line-height: 1.6; color: var(--ink-soft); }
</style>
</head>
<body>
  <p class="label label--section">Stationery Concepts</p>

  <div class="piece card card--front">
    <div class="brand"><span class="brand__dot"></span>Vela Rigs</div>
    <div class="card__details">
      <div class="card__name">Tom Baxter</div>
      <div>Owner/Installation Consultant</div>
      <div>5678 Halloway Dr.</div>
      <div>Alder Falls ON, K7P 5R9</div>
      <div>tom@velarigs.com</div>
      <div>www.velarigs.com</div>
    </div>
  </div>
  <p class="label" style="left:120px; top:329px;">Business Card Front</p>

  <div class="piece card card--back">
    <div class="brand"><span class="brand__dot"></span>Vela Rigs</div>
  </div>
  <p class="label" style="left:120px; top:449px;">Business Card Back</p>

  <div class="piece letterhead">
    <div class="brand brand--top"><span class="brand__dot"></span>Vela Rigs</div>
    <div class="letterhead__contact">
      <div><span></span>5678 Halloway Dr.</div>
      <div>Alder Falls ON, K7P 5R9</div>
      <div><span></span>555-010-0142</div>
      <div><span></span>tom@velarigs.com</div>
      <div><span></span>www.velarigs.com</div>
    </div>
    <div class="letterhead__mark">Vela Rigs</div>
    <svg class="swoosh" viewBox="0 0 399 130" height="130" preserveAspectRatio="none">
      <defs>
        <linearGradient id="lhDark" x1="0" y1="0" x2="0" y2="1">
          <stop offset="0" stop-color="#555"/><stop offset="1" stop-color="#111"/>
        </linearGradient>
      </defs>
      <path d="M0 50 Q200 115 399 25 V130 H0 Z" fill="url(#lhDark)"/>
      <path d="M0 36 Q200 100 399 10" fill="none" stroke="#bbb" stroke-width="1.4"/>
      <path d="M0 66 Q200 125 399 45" fill="none" stroke="#fff" stroke-width="2"/>
    </svg>
  </div>
  <p class="label" style="left:372px; top:577px;">Letter Head Option 1</p>

  <div class="piece envelope envelope--red">
    <svg class="flap" viewBox="0 0 408 100" height="100" preserveAspectRatio="none">
      <defs>
        <radialGradient id="redFlap" cx=".5" cy=".2" r=".7">
          <stop offset="0" stop-color="#d8262c"/><stop offset="1" stop-color="#6e0c0f"/>
        </radialGradient>
      </defs>
      <path d="M0 0 H408 V60 Q204 105 0 60 Z" fill="url(#redFlap)"/>
    </svg>
  </div>

  <div class="piece envelope envelope--dark">
    <svg class="flap" viewBox="0 0 408 120" height="120" preserveAspectRatio="none">
      <defs>
        <radialGradient id="darkFlap" cx=".5" cy=".2" r=".7">
          <stop offset="0" stop-color="#5a5a5a"/><stop offset="1" stop-color="#141414"/>
        </radialGradient>
      </defs>
      <path d="M0 0 H408 V50 Q204 95 0 50 Z" fill="url(#darkFlap)"/>
    </svg>
  </div>

  <div class="piece envelope envelope--white">
    <svg class="flap" viewBox="0 0 408 110" height="110" preserveAspectRatio="none">
      <path d="M0 0 H408 V20 Q204 60 0 20 Z" fill="#ffffff"/>
      <path d="M0 20 Q204 60 408 20" fill="none" stroke="#d8d8d8" stroke-width="1"/>
    </svg>
    <div class="brand"><span class="brand__dot"></span>www.velarigs.com</div>
  </div>

  <div class="piece envelope--front">
    <div class="brand"><span class="brand__dot"></span>Vela Rigs</div>
    <div class="envelope__return">
      <div>5678 Halloway Dr.</div>
      <div>Alder Falls ON, K7P 5R9</div>
    </div>
    <svg class="swoosh" viewBox="0 0 442 70" height="70" preserveAspectRatio="none">
      <defs>
        <linearGradient id="envDark" x1="0" y1="0" x2="0" y2="1">
          <stop offset="0" stop-color="#555"/><stop offset="1" stop-color="#111"/>
        </linearGradient>
      </defs>
      <path d="M0 50 Q220 20 442 10 V70 H0 Z" fill="url(#envDark)"/>
      <path d="M0 58 Q220 28 442 20" fill="none" stroke="#fff" stroke-width="1.6"/>
    </svg>
  </div>
  <p class="label" style="left:883px; top:577px;">Envelope Option 2</p>
</body>
</html>
```